Product Description page for Hullwrap.com, References here just need a clean up redesign

Hi, were working on updating the product description page of our site hullwrap.com

Attached is a reference of what we drew on paint. We want to keep it pretty much the same as far as whats on there, the components with a few small adjustments and a clean actually designed look.

1. We want to remove the tabs (product description, warranty, reviews) and put it all in that main content area stretching down into sections. IE: Product Description section, followed by reviews, followed by warranty, below each other.
2. The side bar needs to be redesigned as far as the look and feel but the content and whats in there should stay the same.
3. The main banner area will be replaced shortly you do not have to worry about that.
4. Include a section or box for people to put in their email for a free Ebook.

Target Market(s)

people looking to easily view our boat cover products and buy without having to click too often or leave the page.

Industry/Entity Type

Online Shopping

Number of Pages Required

1 page

Requirements
Must have
• - Must update the sidebar
• - Must update the content area to remove the tabs and put the content from each tab sectioned off below each other (dummy text is fine for now for the tabs you cant view)
Nice to have
• - Cool place thats clean and functional to insert a section for people to put in their email to receive a free ebook
Should not have
• - too much change, we already know what we want and have a solid reference to work from.

```html
<!DOCTYPE html>
<html lang="en">
<head>
<meta charset="utf-8">
<title>Hullwrap.com – Center Console Boat Cover</title>
<link href="https://fonts.googleapis.com/css2?family=Open+Sans:wght@400;600;700&family=Ubuntu:wght@400;500;700&display=swap" rel="stylesheet">
<style>
:root{
  --blue:#1f7fb8;
  --blue-dark:#0f5a8c;
  --navy:#0c3f73;
  --orange:#ff6a00;
  --orange-dark:#e25500;
  --red:#d0201c;
  --green:#3a9b1a;
  --gold:#f5b400;
  --text:#333;
  --muted:#666;
  --line:#dcdcdc;
  --page:#f4f5f6;
  --card:#e9e9e9;
}
*{box-sizing:border-box;margin:0;padding:0}
html,body{width:1200px;height:3651px;overflow:hidden}
body{background:var(--page);font-family:"Open Sans",sans-serif;color:var(--text);font-size:12.5px;line-height:1.55;position:relative}
.abs{position:absolute}

/* header */
.site-header{left:0;top:0;width:1200px;height:78px;background:#fff}
.brand{left:132px;top:24px;font-family:"Open Sans",sans-serif;font-weight:600;font-size:24px;color:var(--navy);line-height:1.2}
.contact{right:128px;top:10px;text-align:right}
.contact-phone{font-family:"Ubuntu",sans-serif;font-weight:500;font-size:28px;color:var(--blue-dark);display:flex;align-items:center;gap:8px;line-height:1.1}
.contact-hours{font-size:11px;color:var(--muted)}

.main-nav{left:0;top:78px;width:1200px;height:40px;background:linear-gradient(#f4f4f4,#dedede);border-top:1px solid #ccc;border-bottom:1px solid #bbb}
.main-nav ul{list-style:none;display:flex;position:absolute;left:128px;top:0;height:38px}
.main-nav li{font-family:"Ubuntu",sans-serif;font-size:15px;color:#333;padding:0 24px;line-height:38px;border-right:1px solid #c9c9c9}
.main-nav li:first-child{padding-left:2px}
.checkout{position:absolute;right:128px;top:6px;height:27px;width:188px;background:linear-gradient(#3a8fd0,#1b5f9c);border-radius:3px;color:#fff;font-size:12px;font-weight:700;display:flex;align-items:center;gap:8px;padding-left:10px}

.breadcrumb{left:0;top:118px;width:1200px;height:38px;background:#eceff1;font-size:12px;line-height:38px;padding-left:128px;color:#333}
.breadcrumb .cur{color:var(--blue)}

/* product hero */
.product{left:128px;top:175px;width:944px;height:502px}
.gallery{left:0;top:0;width:616px;height:502px;background:#fff;border:1px solid var(--line)}
.gallery-main{position:absolute;left:20px;top:20px;width:576px;height:390px;background:radial-gradient(ellipse at 50% 55%,#d9dcdf 0%,#eef0f1 45%,#fff 75%)}
.thumbs{position:absolute;left:20px;top:418px;width:576px;height:66px;display:flex;align-items:center;gap:8px}
.thumb-arrow{width:22px;height:66px;background:#e3e3e3;display:flex;align-items:center;justify-content:center}
.thumb{width:62px;height:62px}
.buybox{left:640px;top:0;width:304px;height:502px;background:#fff;border:1px solid var(--line);padding:16px 14px}
.buybox h1{font-family:"Ubuntu",sans-serif;font-size:20px;font-weight:700;line-height:1.25;color:#222}
.price{font-size:24px;font-weight:700;color:var(--red);margin-top:10px;font-family:"Ubuntu",sans-serif}
.price-meta{font-size:12px;color:var(--muted);margin-top:10px;line-height:1.45}
.rating{margin-top:10px;font-size:22px;color:var(--gold);letter-spacing:1px;display:flex;align-items:center;gap:6px;padding-bottom:10px;border-bottom:1px solid var(--line)}
.rating span{font-size:20px;color:var(--gold);font-family:"Ubuntu",sans-serif}
.stock{display:flex;border-bottom:1px solid var(--line);font-size:12px;padding:8px 0}
.stock div{flex:1;line-height:1.4}
.option{display:flex;align-items:center;gap:14px;font-size:12px;padding:14px 0;border-bottom:1px solid var(--line)}
.select{border:1px solid #bbb;border-radius:2px;padding:2px 8px;font-size:12px;background:#fafafa}
.btn-cart{display:flex;align-items:center;justify-content:center;gap:10px;background:var(--orange);color:#fff;font-family:"Ubuntu",sans-serif;font-weight:700;font-size:16px;border-radius:3px;letter-spacing:.5px}
.buybox .btn-cart{height:44px;margin-top:14px}
.free-ship{color:var(--green);font-size:13px;font-weight:600;text-align:center;margin-top:8px;display:flex;justify-content:center;align-items:center;gap:6px}

/* sections */
.section{left:128px;width:618px}
.section-tab{position:relative;height:38px;border-bottom:3px solid var(--blue)}
.section-tab span{display:inline-block;height:38px;line-height:38px;padding:0 42px 0 18px;background:var(--blue);color:#fff;font-family:"Ubuntu",sans-serif;font-weight:500;font-size:16px;clip-path:polygon(0 0,86% 0,100% 100%,0 100%)}
.section-body{background:#fff;border:1px solid var(--line);border-top:none;padding:14px 18px 18px}
.section-body h3{font-family:"Ubuntu",sans-serif;font-size:15px;font-weight:700;color:#222;margin:14px 0 8px}
.section-body h3:first-child{margin-top:0}
.section-body p{margin-bottom:12px;color:#444}
.features{list-style:none}
.features li{color:#444;line-height:1.75}
.features li::before{content:"– "}

.review{padding:12px 0;border-bottom:1px solid var(--line)}
.review-name{font-weight:700;font-size:13px;color:#222}
.review-name b{color:var(--gold);letter-spacing:1px;margin-left:6px}
.review p{font-style:italic;margin:8px 0 0}
.review-form{margin-top:20px;background:#e6e6e6;padding:12px 14px 22px;border-radius:2px}
.review-form .inner{background:#fff;padding:12px 14px 18px}
.review-form h4{font-size:13px;font-weight:600}
.review-form .sub{font-size:12px;color:#555;padding-bottom:10px;border-bottom:1px solid var(--line)}
.field{position:relative;margin-top:12px;border:1px solid #bbb;height:38px;padding:8px 10px;font-size:12px;color:#666;width:538px}
.field.tall{height:82px}
.field::after{content:"*";position:absolute;right:-12px;top:-2px;color:var(--red)}
.btn-submit{margin-top:14px;width:140px;height:38px;background:var(--orange);color:#fff;font-weight:700;font-size:12px;display:flex;align-items:center;justify-content:center;border-radius:3px}

/* sidebar */
.sidebar{left:768px;top:713px;width:304px}
.sidebar-title{height:40px;background:var(--blue);color:#fff;font-family:"Ubuntu",sans-serif;font-weight:700;font-size:17px;text-align:center;line-height:40px;border-radius:3px;letter-spacing:.5px}
.rec-card{position:absolute;left:0;width:304px;height:368px;background:var(--card);padding:14px 18px}
.rec-img{width:268px;height:168px;background:radial-gradient(ellipse at 50% 55%,#d6d9dc 0%,#eef0f1 50%,#fff 80%)}
.rec-card h5{font-size:12.5px;font-weight:400;margin-top:10px;line-height:1.4;color:#222}
.rec-card .btn-cart{height:32px;font-size:13px;margin-top:6px}
.rec-meta{font-size:11.5px;margin-top:8px;line-height:1.55}
.rec-meta .ship{color:var(--orange-dark)}
.rec-meta .stars{color:var(--gold);letter-spacing:1px}

/* newsletter */
.newsletter{left:128px;top:3193px;width:944px;height:94px;background:#fff;border:1px solid var(--line);border-radius:4px}
.newsletter h2{position:absolute;left:30px;top:16px;font-family:"Ubuntu",sans-serif;font-size:28px;font-weight:700;color:var(--blue-dark);line-height:1.05}
.newsletter .lead{position:absolute;left:30px;top:52px;font-family:"Ubuntu",sans-serif;font-size:17px;color:#333}
.nl-form{position:absolute;left:434px;top:22px;width:500px;height:50px;background:#eceded;border-radius:25px;border:1px solid #d5d5d5}
.nl-form .ph{position:absolute;left:22px;top:14px;font-size:14px;color:#555}
.nl-btn{position:absolute;right:6px;top:5px;width:150px;height:38px;border-radius:19px;background:linear-gradient(#8fc43a,#5f9b15);color:#fff;font-family:"Ubuntu",sans-serif;font-weight:700;font-size:15px;display:flex;align-items:center;justify-content:center;letter-spacing:.5px}

/* footer */
.footer-scene{left:0;top:3340px;width:1200px;height:178px;background:linear-gradient(#f4f5f6 0%,#c9d6e0 25%,#8aa0b6 55%,#4c6883 75%,#1e3c5e 100%)}
.footer-bar{left:0;top:3518px;width:1200px;height:50px;background:linear-gradient(#0d4f8e,#073766);color:#fff}
.footer-bar .win{position:absolute;left:145px;top:15px;font-size:13px;font-weight:700}
.footer-bar .input{position:absolute;left:375px;top:14px;width:180px;height:22px;background:#fff}
.footer-bar .sub{position:absolute;left:558px;top:14px;width:80px;height:22px;background:var(--orange);font-size:11px;font-weight:700;display:flex;align-items:center;justify-content:center}
.footer-bar .links{position:absolute;right:148px;top:15px;font-size:13px;font-weight:700;display:flex;gap:28px;text-decoration:underline}
.footer-copy{left:0;top:3568px;width:1200px;height:83px;background:#061c35;color:#7f95ad;text-align:center;font-size:11px;line-height:1.5;padding-top:22px}
.footer-copy u{color:#c7d3df}
</style>
</head>
<body>

<header class="site-header abs">
  <div class="brand abs">Hullwrap.com</div>
  <div class="contact abs">
    <div class="contact-phone">
      <svg width="24" height="24" viewBox="0 0 24 24"><path fill="#0f5a8c" d="M6.6 10.8a15 15 0 0 0 6.6 6.6l2.2-2.2c.3-.3.7-.4 1-.2 1.1.4 2.3.6 3.6.6.6 0 1 .4 1 1V20c0 .6-.4 1-1 1C10.6 21 3 13.4 3 4c0-.6.4-1 1-1h3.5c.6 0 1 .4 1 1 0 1.3.2 2.5.6 3.6.1.3 0 .7-.2 1z"/></svg>
      (800) 555-0142
    </div>
    <div class="contact-hours">Store Hours M-F, 9:30AM – 6PM (PST)</div>
  </div>
</header>

<nav class="main-nav abs">
  <ul>
    <li>Boat Covers</li>
    <li>Bass Boat Covers</li>
    <li>T-Top/Hard Top</li>
    <li>Bimini Tops</li>
    <li>Jet Ski Covers</li>
  </ul>
  <div class="checkout">
    <svg width="18" height="16" viewBox="0 0 18 16"><path fill="#fff" d="M0 1h3l2.5 9h9l2-7H5V1.5"/><circle cx="7" cy="13.5" r="1.6" fill="#fff"/><circle cx="13" cy="13.5" r="1.6" fill="#fff"/></svg>
    CHECKOUT : (0) Items ▾
  </div>
</nav>

<div class="breadcrumb abs">Home &gt; Boat Covers &gt; Center Console without Bow Rails &gt; <span class="cur">up to 15'8" Long and 96" Wide</span></div>

<section class="product abs">
  <div class="gallery abs">
    <div class="gallery-main" role="img" aria-label="Grey boat cover fitted over a center console boat on a trailer"></div>
    <div class="thumbs">
      <div class="thumb-arrow"><svg width="8" height="14"><path d="M7 1L1 7l6 6" stroke="#777" stroke-width="2" fill="none"/></svg></div>
      <div class="thumb" role="img" aria-label="Cover storage bag" style="background:#8b3b2d"></div>
      <div class="thumb" role="img" aria-label="Blue cover fabric" style="background:#2d5fa3"></div>
      <div class="thumb" role="img" aria-label="Cover fabric detail" style="background:#8fa3bb"></div>
      <div class="thumb" role="img" aria-label="Tie-down strap" style="background:#6a6e73"></div>
      <div class="thumb" role="img" aria-label="Buckle detail" style="background:#3d4044"></div>
      <div class="thumb" role="img" aria-label="Strap and hardware" style="background:#9a9ea3"></div>
      <div class="thumb" role="img" aria-label="Cover on boat side view" style="background:#d8dadd"></div>
      <div style="flex:1"></div>
      <div class="thumb-arrow"><svg width="8" height="14"><path d="M1 1l6 6-6 6" stroke="#777" stroke-width="2" fill="none"/></svg></div>
    </div>
  </div>
  <div class="buybox abs">
    <h1>Fits: Center Console without Bow Rails up to 15'8" Long and 96" Wide</h1>
    <div class="price">$292.50</div>
    <div class="price-meta">Regular Price: $435.50<br>You Save: $143.00</div>
    <div class="rating">★★★★★ <span>(1,500)</span></div>
    <div class="stock"><div>Availability:<br>Ready to Ship</div><div>Ships:<br>1 Business Day</div></div>
    <div class="option">Color: <span class="select">Choose an Option... ▾</span></div>
    <div class="option" style="border:none;padding-bottom:0">Quantity: <span class="select">1 ▾</span></div>
    <div class="btn-cart">ADD TO CART
      <svg width="24" height="20" viewBox="0 0 18 16"><path fill="#fff" d="M0 1h3l2.5 9h9l2-7H5V1.5"/><circle cx="7" cy="13.5" r="1.6" fill="#fff"/><circle cx="13" cy="13.5" r="1.6" fill="#fff"/></svg>
    </div>
    <div class="free-ship">
      <svg width="22" height="14" viewBox="0 0 22 14"><path fill="#3a9b1a" d="M0 1h13v9H0zM14 4h4l3 3v3h-7z"/><circle cx="4" cy="11.5" r="2" fill="#3a9b1a"/><circle cx="17" cy="11.5" r="2" fill="#3a9b1a"/></svg>
      Free Shipping!
    </div>
  </div>
</section>

<section class="section abs" style="top:713px">
  <div class="section-tab"><span>Product Info</span></div>
  <div class="section-body" style="height:429px">
    <h3>Description:</h3>
    <p>When a boat is stored outside it is exposed to harmful elements such as wind, dirt, rain, and UV. The Tidewarden Supreme is the most powerful cover available providing 10x more strength and protection compared to the competition. The 1200 denier fabric is 100% waterproof and provides excellent protection against sun, rain, wind and snow.</p>
    <h3>Features:</h3>
    <ul class="features">
      <li>5 Star Fit, Fit guaranteed or your money back</li>
      <li>10 Year Warranty: Full warranty covering rips and tears</li>
      <li>The covers comes in Grey, Blue and Maroon</li>
      <li>The fabric is pure 100% Marine Polyester (no cotton mix)</li>
      <li>No worries, the cover won't stretch or shrink</li>
      <li>Rain or sleet the cover is 100% waterproof</li>
      <li>Fully Breathable, you'll never see mold or mildew</li>
      <li>UV resistant and also prevents heat buildup</li>
      <li>Fully Trailerable (straps included)</li>
      <li>The cover also comes with an integrated hem cord to be used when mooring or on boat lifts</li>
      <li>Tough - Strong - Durable</li>
    </ul>
  </div>
</section>

<section class="section abs" style="top:1208px">
  <div class="section-tab"><span>Reviews</span></div>
  <div class="section-body" style="height:779px;padding-top:4px">
    <div class="review"><div class="review-name">Marcus J. <b>★★★★</b></div><p>"This item is quite heavy duty and rides well. It is also great quality. We are pleased with the cover and I would recommend it to anyone who wants a great fit and strong cover."</p></div>
    <div class="review"><div class="review-name">Dale <b>★★★★★</b></div><p>"I have this on my runabout and it fits great, I feel better with my boat covered and this is a very nice cover. The price was nice especially if you have seen the price on factory covers. I would definitely buy this again and recommend to anyone with boat."</p></div>
    <div class="review"><div class="review-name">Ruben <b>★★★★★</b></div><p>"I bought 2 of these for 2 boats I own. They have been fabulous so far. We will see how they survive the winter."</p></div>
    <div class="review" style="border:none"><div class="review-name">Ruben <b>★★★★★</b></div><p>"I bought 2 of these for 2 boats I own. They have been fabulous so far. We will see how they survive the winter."</p></div>
    <div class="review-form">
      <div class="inner">
        <h4>Write Your Own Review</h4>
        <div class="sub">You're reviewing: Tidewarden Supreme Boat Cover™</div>
        <div class="field">Nickname</div>
        <div class="field">Summary of Your Review</div>
        <div class="field tall">Review</div>
        <div class="btn-submit">SUBMIT REVIEW</div>
      </div>
    </div>
  </div>
</section>

<section class="section abs" style="top:2063px">
  <div class="section-tab"><span>Warranty</span></div>
  <div class="section-body" style="height:606px">
    <h3>Returns &amp; Refunds</h3>
    <p>If you are not 100% satisfied with your purchase, you can return or exchange your order. (Returns must be unworn, in the state you received them, and in the original packaging).</p>
    <p>Harbor Value Covers will process all returns and refunds within 30 days of original order date. After 30 days all orders are final. For the full details on our returns or exchange policy please read below.</p>
    <p>Harbor Value Covers guarantees the covers you purchase will arrive in new condition, be free of defects and will properly fit the vehicle for which you ordered. If your item fails to meet the criteria above Harbor Value Covers will exchange or return the item.</p>
    <h3>Returning Tidewarden Supreme Covers</h3>
    <p>Tidewarden Supreme covers are 5 Star Fit Covers. The fit and quality are 100% guaranteed or your money back. You have 30 days to try the cover. If you are not 100% satisfied feel free to return or exchange it hassle free. No restocking fee's, we even pay for the shipping.</p>
    <h3>Returning MarinaPro Covers</h3>
    <p>MarinaPro covers are 4 Star Fit Covers. MarinaPro covers are semi custom covers based on boat style, length and width. The cover is fully exchangeable.. A small 15% restocking fee is applied when returning or exchanging this cover. You have 30 days to return or exchange the cover. If you are not 100% satisfied, give us a call and will help return or exchange it. We even pay for the shipping.</p>
    <h3>Returning Sunfield Covers</h3>
    <p>Sunfield covers are 3 Star Fit Covers. Sunfield covers are universal covers based on length and width. A small 15% restocking fee is applied when returning or exchanging this cover. You have 30 days to return or exchange the cover. If you are not 100% satisfied, give us a call and will help return or exchange it. We even pay for the shipping.</p>
  </div>
</section>

<section class="section abs" style="top:2730px">
  <div class="section-tab"><span>Shipping</span></div>
  <div class="section-body" style="height:410px">
    <h3>Returns &amp; Refunds</h3>
    <p>Unlike many other web sites that have special rules and lots of fine print, Harbor Value Covers offers free shipping on all domestic orders placed on our website.</p>
    <p>Just because shipping is free doesn't mean it should take a long time. We understand that getting your items quickly is important to you, so we make every effort to process your order quickly. When you order from our website, you can expect to receive your order within 4-5 business days.</p>
    <p>If an error is found in the shipping address, please contact us at 1-800-555-0142 as soon as possible and our Support Staff will do their best to update your order with the correct shipping information or intercept the package and correct the destination if it has already shipped.</p>
    <h3>Shipping Internationally</h3>
    <p>We will gladly ship your product to Canada; however, these orders are not eligible for free shipping and may be subject to customs fees, taxes, or duties. These fees are not determined until the product crosses the border; therefore, these costs are the responsibility of the customer. Our shipping and handling cost does not include any of these fees.</p>
  </div>
</section>

<aside class="sidebar abs">
  <div class="sidebar-title">YOU MAY ALSO LIKE</div>
  <div class="rec-card" style="top:56px">
    <div class="rec-img" role="img" aria-label="Grey boat cover on a center console boat with bow rails"></div>
    <h5>Fits: Center Console with Bow Rails up to 17'8" Long and 92" Wide</h5>
    <div class="btn-cart">ADD TO CART <svg width="18" height="16" viewBox="0 0 18 16"><path fill="#fff" d="M0 1h3l2.5 9h9l2-7H5V1.5"/><circle cx="7" cy="13.5" r="1.6" fill="#fff"/><circle cx="13" cy="13.5" r="1.6" fill="#fff"/></svg></div>
    <div class="rec-meta">From $331.50<br><span class="ship">Free Shipping!</span><br>Rating <span class="stars">★★★★★</span> (1K+)</div>
  </div>
  <div class="rec-card" style="top:446px">
    <div class="rec-img" role="img" aria-label="Grey boat cover on a center console boat with bow rails"></div>
    <h5>Fits: Center Console with Bow Rails up to 17'8" Long and 92" Wide</h5>
    <div class="btn-cart">ADD TO CART <svg width="18" height="16" viewBox="0 0 18 16"><path fill="#fff" d="M0 1h3l2.5 9h9l2-7H5V1.5"/><circle cx="7" cy="13.5" r="1.6" fill="#fff"/><circle cx="13" cy="13.5" r="1.6" fill="#fff"/></svg></div>
    <div class="rec-meta">From $331.50<br><span class="ship">Free Shipping!</span><br>Rating <span class="stars">★★★★★</span> (1K+)</div>
  </div>
  <div class="rec-card" style="top:828px">
    <div class="rec-img" role="img" aria-label="Grey boat cover on a center console boat with bow rails"></div>
    <h5>Fits: Center Console with Bow Rails up to 17'8" Long and 92" Wide</h5>
    <div class="btn-cart">ADD TO CART <svg width="18" height="16" viewBox="0 0 18 16"><path fill="#fff" d="M0 1h3l2.5 9h9l2-7H5V1.5"/><circle cx="7" cy="13.5" r="1.6" fill="#fff"/><circle cx="13" cy="13.5" r="1.6" fill="#fff"/></svg></div>
    <div class="rec-meta">From $331.50<br><span class="ship">Free Shipping!</span><br>Rating <span class="stars">★★★★★</span> (1K+)</div>
  </div>
  <div class="rec-card" style="top:1207px">
    <div class="rec-img" role="img" aria-label="Grey boat cover on a center console boat with bow rails"></div>
    <h5>Fits: Center Console with Bow Rails up to 17'8" Long and 92" Wide</h5>
    <div class="btn-cart">ADD TO CART <svg width="18" height="16" viewBox="0 0 18 16"><path fill="#fff" d="M0 1h3l2.5 9h9l2-7H5V1.5"/><circle cx="7" cy="13.5" r="1.6" fill="#fff"/><circle cx="13" cy="13.5" r="1.6" fill="#fff"/></svg></div>
    <div class="rec-meta">From $331.50<br><span class="ship">Free Shipping!</span><br>Rating <span class="stars">★★★★★</span> (1K+)</div>
  </div>
</aside>

<section class="newsletter abs">
  <h2>Subscribe to our Newsletter</h2>
  <div class="lead">and email to receive a free ebook</div>
  <div class="nl-form"><span class="ph">Enter Your Email</span><div class="nl-btn">SIGN UP</div></div>
</section>

<div class="footer-scene abs" role="img" aria-label="Marina with moored boats on a lake in front of misty mountains"></div>

<footer>
  <div class="footer-bar abs">
    <span class="win">Sign Up To Win A FREE Boat Cover!</span>
    <span class="input"></span>
    <span class="sub">Subscribe ›</span>
    <span class="links"><span>Exchanges &amp; Returns</span><span>Contact Us</span></span>
  </div>
  <div class="footer-copy abs">
    Copyright © 2016 Hullwrap.com. All Rights Reserved.<br>
    214 Pier Lane, Bayport NY 11705<br>
    <u>Privacy Policy</u>
  </div>
</footer>

</body>
</html>
```